Layout of a white paper from an already written word document

We are a consulting company specializing in General Data Protection Regulation (GDPR) and cybersecurity. We wish to publish a white paper on our methodologies. The text is ready and we would like it to be laid out in a neat design.
Our target is SMEs and mid-caps.
We try to provide very concrete and pragmatic solutions to our clients. Attached is a sample white paper that we appreciate and the text to format.
Our web site: www.harbor-quill.com
Target Market(s)
SMEs and mid-caps
Requirements
Must have
- A4 Format

```html
<!DOCTYPE html>
<html lang="fr">
<head>
<meta charset="utf-8">
<title>RGPD et Cyberattaques – Livre blanc</title>
<link rel="stylesheet" href="https://fonts.googleapis.com/css2?family=Montserrat:wght@700;800&family=Open+Sans:wght@400;600&display=swap">
<style>
  :root {
    --backdrop: #1e1e1e;
    --paper: #ffffff;
    --brand-blue: #0db6e0;
    --brand-blue-soft: #bfeaf6;
    --brand-green: #b8d14a;
    --heading-green: #a5c83a;
    --ink: #2a2a2a;
    --ink-body: #15303d;
  }
  * { box-sizing: border-box; margin: 0; padding: 0; }
  html, body { width: 884px; height: 1200px; overflow: hidden; background: var(--backdrop); }
  .canvas { position: relative; width: 884px; height: 1200px; }

  .page {
    position: absolute;
    left: 305px;
    width: 510px;
    height: 659px;
    background: var(--paper);
    overflow: hidden;
    transform: scale(0.535);
    transform-origin: 0 0;
    font-family: "Open Sans", Arial, sans-serif;
  }
  .page--cover { top: 57px; }
  .page--context { top: 424px; }
  .page--actions { top: 790px; }

  .cover-decor {
    position: absolute;
    left: 0; top: 330px;
    width: 510px; height: 329px;
    background: linear-gradient(160deg, var(--paper) 0%, var(--brand-blue-soft) 30%, var(--brand-blue) 62%, var(--brand-green) 63%, var(--brand-green) 100%);
  }
  .footer-decor {
    position: absolute;
    left: 0; bottom: 0;
    width: 510px; height: 90px;
    background: linear-gradient(90deg, var(--paper) 0%, var(--brand-blue-soft) 45%, var(--brand-blue) 100%);
  }

  .brand {
    position: absolute;
    display: flex;
    flex-direction: column;
    align-items: center;
    gap: 8px;
    font-family: "Montserrat", Arial, sans-serif;
    font-weight: 700;
    color: var(--brand-blue);
    text-align: center;
    line-height: 1.05;
    letter-spacing: 0.5px;
  }
  .brand__dot { border-radius: 50%; background: var(--brand-blue); }
  .page--cover .brand { left: 368px; top: 42px; font-size: 17px; }
  .page--cover .brand__dot { width: 52px; height: 52px; }
  .page--context .brand { left: 22px; top: 32px; font-size: 13px; }
  .page--context .brand__dot { width: 44px; height: 44px; }
  .page--actions .brand { left: 16px; top: 18px; font-size: 13px; }
  .page--actions .brand__dot { width: 40px; height: 40px; }

  .cover-title {
    position: absolute;
    left: 123px;
    top: 238px;
    font-family: "Montserrat", Arial, sans-serif;
    font-weight: 800;
    font-size: 24.5px;
    line-height: 34px;
    color: var(--ink);
  }
  .cover-url {
    position: absolute;
    left: 343px;
    top: 603px;
    font-family: "Montserrat", Arial, sans-serif;
    font-weight: 700;
    font-size: 10.5px;
    color: var(--ink);
  }

  .section-title {
    position: absolute;
    left: 107px;
    top: 155px;
    width: 310px;
    font-family: "Montserrat", Arial, sans-serif;
    font-weight: 800;
    font-size: 19px;
    line-height: 25px;
    color: var(--heading-green);
  }
  .context-band {
    position: absolute;
    left: 0; top: 240px;
    width: 510px; height: 419px;
    background: var(--brand-blue);
  }
  .body-copy {
    position: absolute;
    left: 107px;
    width: 360px;
    font-size: 9.3px;
    line-height: 13.6px;
    color: var(--ink-body);
  }
  .page--context .body-copy { top: 270px; }
  .page--actions .body-copy { top: 112px; }
  .body-copy p { margin-bottom: 7px; }
  .body-copy ul, .body-copy ol { list-style: none; margin-left: 12px; }
  .body-copy li { position: relative; padding-left: 18px; margin-bottom: 7px; }
  .body-copy ul li::before { content: "-"; position: absolute; left: 0; }
  .body-copy ol { counter-reset: step; }
  .body-copy ol li { counter-increment: step; }
  .body-copy ol li::before { content: counter(step) "."; position: absolute; left: 0; }

  .folio {
    position: absolute;
    left: 0; bottom: 0;
    width: 510px; height: 50px;
  }
  .folio__title {
    position: absolute;
    right: 73px; top: 4px;
    font-family: "Montserrat", Arial, sans-serif;
    font-weight: 800;
    font-size: 5.4px;
    line-height: 7px;
    text-align: right;
    color: var(--ink);
  }
  .folio__rule {
    position: absolute;
    left: 444px; top: 0;
    width: 1px; height: 50px;
    background: var(--ink);
  }
  .folio__number {
    position: absolute;
    left: 458px; top: 3px;
    font-family: "Montserrat", Arial, sans-serif;
    font-weight: 800;
    font-size: 8px;
    color: var(--ink);
  }
</style>
</head>
<body>
<main class="canvas">

  <section class="page page--cover">
    <div class="cover-decor" role="img" aria-label="Décor graphique en dégradé bleu et vert"></div>
    <div class="brand"><span class="brand__dot"></span><span>HARBOR<br>QUILL</span></div>
    <h1 class="cover-title">RGPD et Cyberattaques<br>4 actions pour assurer<br>et rassurer</h1>
    <p class="cover-url">www.harbor-quill.com</p>
  </section>

  <section class="page page--context">
    <div class="context-band"></div>
    <div class="brand"><span class="brand__dot"></span><span>HARBOR<br>QUILL</span></div>
    <h2 class="section-title">Modèle de maturité CPDN et Cyberattaques: 4 actions pour rassurer</h2>
    <div class="body-copy">
      <p>Initier une nouvelle auto-évaluation avec le modèle de maturité publié par la CPDN le 9 septembre 2021</p>
      <p>En quelques mois, à cause et grâce au Covid, le marché a gagné en maturité et en expérience, ce qui a conduit les acteurs de la conformité et les régulateurs, dont la CPDN avec son modèle de maturité publié le 9 septembre 2021, à mettre à disposition des organisations, des outils qui permettent aux organisations d'engager des actions concrètes et pragmatiques leur permettant de faire face.</p>
      <p>Dans ce contexte, plusieurs constats permettent de comprendre l'urgence d'agir :</p>
      <ul>
        <li>Depuis le Covid, les services d'audit interne multiplient leurs interventions et déplorent que les entreprises sous-traitantes ne respectent pas la réglementation et ne disposent pas de mesures de sécurité susceptibles de protéger leurs clients.</li>
        <li>La concurrence entre entreprises sous-traitantes n'a jamais été aussi tendue, ce qui autorise les acheteurs à augmenter leur niveau d'exigence en imposant des demandes qui paraissaient déraisonnables il y a encore quelques mois.</li>
        <li>Bon nombre de sinistres cybers analysés par les compagnies d'assurances ont fait apparaître des lacunes en matière de conformité et de sécurité qu'elles refusent désormais de couvrir.</li>
      </ul>
    </div>
    <footer class="folio">
      <p class="folio__title">RGPD et Cyberattaques 4 actions<br>pour assurer et rassurer</p>
      <span class="folio__rule"></span>
      <span class="folio__number">2</span>
    </footer>
  </section>

  <section class="page page--actions">
    <div class="footer-decor" role="img" aria-label="Bandeau décoratif en dégradé bleu"></div>
    <div class="brand"><span class="brand__dot"></span><span>HARBOR<br>QUILL</span></div>
    <div class="body-copy">
      <p>Nous avons identifié ainsi quatre actions prioritaires pour assurer et rassurer efficacement clients, utilisateurs et investisseurs :</p>
      <ol>
        <li>Initier une nouvelle auto-évaluation avec le modèle de maturité publié par la CPDN le 9 septembre 2021</li>
        <li>Mettre en place des indicateurs objectifs en matière de sécurité, en s'appuyant sur des outils qui permettent de disposer d'une notation sécurité par une tierce partie et notamment des outils tels que ScoreVigil ou Notarisk.</li>
        <li>Mettre en place et faire vivre un dossier de conformité solide adapté aux spécificités de l'entreprise, incluant les 61 mesures du modèle de la CPDN dont on extraira les éléments clés pour mettre à la disposition des équipes commerciales une base de connaissance les aidant à répondre aux clients et aux prospects et ainsi ne pas perdre de marchés.</li>
        <li>Mixer des compétences internes (savoir-faire métier) et externes (expertise RGPD, cybersécurité) pour garantir une réelle expertise (capacité à se protéger et protéger ses partenaires contre les attaques malveillantes) et être capable de faire face à la variabilité de la demande.</li>
      </ol>
    </div>
    <footer class="folio">
      <p class="folio__title">RGPD et Cyberattaques 4 actions<br>pour assurer et rassurer</p>
      <span class="folio__rule"></span>
      <span class="folio__number">3</span>
    </footer>
  </section>

</main>
</body>
</html>
```